Lumora business card for a plastic surgeon

we need a business card for plastic surgeons that work on a clinic called LUMORA.
we want a clean design and the following informations: name of the doctor, doctor's registration number (called CRM), telephone, address, facebook, instagram.
Colors: white, blue tones, light brown/ coffee

facebook and instagram: lumoraesteticaclinica

Industry/Entity Type

Business

Contact Information for Business Card

clean design

Font styles to use
Serif
Sans Serif
Other font styles liked:
• helvetica light

Colors
cee9f5
85cae6
85abd2
3276b5
cfeae6
cedeed
eaf1f7

Requirements
Must have
• doctor's name
• identification number (called CRM)
• contact (phone, facebook, instagram, address)

```html
<!DOCTYPE html>
<html lang="en">
<head>
<meta charset="utf-8">
<title>Lumora — Business Card</title>
<link rel="stylesheet" href="https://fonts.googleapis.com/css2?family=Open+Sans:wght@400;600;700&display=swap">
<style>
  :root {
    --bg: #e4e7ea;
    --cyan: #25b9d7;
    --navy: #0e3a66;
    --white: #ffffff;
    --grey: #6b6b6b;
    --fold: #c9cfd4;
    --shadow: rgba(20, 40, 60, 0.18);
  }
  * { margin: 0; padding: 0; box-sizing: border-box; }
  html, body { width: 1200px; height: 900px; overflow: hidden; }
  body {
    background: var(--bg);
    font-family: "Open Sans", Arial, sans-serif;
    position: relative;
  }
  .card {
    position: absolute;
    left: 250px;
    width: 700px;
    height: 400px;
    border-radius: 26px;
    overflow: hidden;
    box-shadow: 0 10px 30px var(--shadow);
  }
  .card--back { top: 30px; background: var(--cyan); }
  .card--front { top: 470px; background: var(--white); }

  .brand {
    position: absolute;
    display: flex;
    align-items: center;
    gap: 14px;
    font-weight: 400;
    letter-spacing: 6px;
    white-space: nowrap;
  }
  .brand__dot { width: 16px; height: 16px; border-radius: 50%; flex: none; }
  .card--back .brand {
    left: 0; right: 0; top: 160px; justify-content: center;
    font-size: 64px; color: var(--white);
  }
  .card--back .brand__dot { background: var(--white); }
  .card--front .brand {
    left: 20px; width: 340px; top: 150px; justify-content: center;
    font-size: 48px; color: var(--cyan);
  }
  .card--front .brand__dot { background: var(--cyan); }

  .social {
    position: absolute; left: 60px; top: 318px;
    display: flex; align-items: center; gap: 10px;
    font-size: 19px; color: var(--grey); white-space: nowrap;
  }
  .social__dot { width: 20px; height: 20px; border-radius: 50%; background: var(--cyan); flex: none; }

  .panel { position: absolute; left: 412px; top: 0; width: 288px; height: 400px; background: var(--cyan); }
  .stripe { position: absolute; left: 380px; top: 0; width: 32px; height: 400px; background: var(--navy); }

  .name-band {
    position: absolute; left: 412px; top: 72px; width: 288px; height: 64px;
    background: var(--white); padding: 6px 0 0 18px;
  }
  .name-band__fold { position: absolute; left: 344px; top: 118px; }
  .doctor { font-size: 18px; font-weight: 700; color: var(--navy); white-space: nowrap; }
  .doctor__title { color: var(--cyan); font-weight: 600; }
  .position { font-size: 16px; color: var(--grey); }

  .crm { position: absolute; left: 430px; top: 150px; font-size: 11px; color: var(--white); }
  .address {
    position: absolute; left: 430px; top: 184px;
    font-size: 16px; line-height: 23px; color: var(--white); white-space: nowrap;
  }
  .contacts { position: absolute; left: 380px; top: 250px; list-style: none; }
  .contacts li {
    display: flex; align-items: center; height: 28px;
    font-size: 16px; color: var(--white); white-space: nowrap;
  }
  .contacts .icon { width: 32px; display: flex; justify-content: center; margin-right: 14px; flex: none; }
  .contacts svg { width: 16px; height: 16px; }
</style>
</head>
<body>

  <section class="card card--back" aria-label="Card back">
    <div class="brand"><span class="brand__dot"></span>LUMORA</div>
  </section>

  <section class="card card--front" aria-label="Card front">
    <div class="brand"><span class="brand__dot"></span>LUMORA</div>

    <div class="social"><span class="social__dot"></span>/lumoraesteticaclinica</div>

    <div class="panel"></div>
    <div class="stripe"></div>

    <svg class="name-band__fold" width="36" height="18" viewBox="0 0 36 18" aria-hidden="true">
      <polygon points="0,0 36,0 36,18" fill="#c9cfd4"/>
    </svg>
    <div class="name-band">
      <p class="doctor"><span class="doctor__title">Dr. LUCAS</span> ABRANTES</p>
      <p class="position">Your Position</p>
    </div>

    <p class="crm">CRM: 34 620 518 207</p>
    <p class="address">1470 North Cedar Crest Rd<br>Suite 210-318 Fairview, AZ</p>

    <ul class="contacts">
      <li><span class="icon"><svg viewBox="0 0 16 16"><path d="M3 1l3 3-1.6 1.8c.9 2 2.5 3.6 4.6 4.6L11 9l3 3-2 2.4C6.5 14 2 9.5 1.6 3z" fill="#fff"/></svg></span>0455210876</li>
      <li><span class="icon"><svg viewBox="0 0 16 16"><circle cx="8" cy="8" r="6" fill="none" stroke="#fff" stroke-width="1.6"/></svg></span>0455210876</li>
      <li><span class="icon"><svg viewBox="0 0 16 16"><rect x="1" y="3" width="14" height="10" fill="none" stroke="#fff" stroke-width="1.4"/><path d="M1 3l7 6 7-6" fill="none" stroke="#fff" stroke-width="1.4"/></svg></span>info@lumoraesteticaclinica</li>
      <li><span class="icon"><svg viewBox="0 0 16 16"><circle cx="8" cy="8" r="6.5" fill="none" stroke="#fff" stroke-width="1.3"/><ellipse cx="8" cy="8" rx="3" ry="6.5" fill="none" stroke="#fff" stroke-width="1.1"/><path d="M1.5 8h13M2.5 5h11M2.5 11h11" stroke="#fff" stroke-width="1"/></svg></span>www.lumoraesteticaclinica.com</li>
    </ul>
  </section>

</body>
</html>
```